Brand Identity Stationary Package

Hello I'm looking for a full branding package for my Property Management Company. I have a logo but looking to have the following
Business Card
Email signature
Facebook cover photo
Letterhead (word.doc)
#10 Envelope
Pocket Folder - link to 9x12 pocket folder design specs https://www.quillpress.ca/marketing-materials/presentation-folders
would like everything to match and be brand identifiable. The company looks after residential properties/apartments and some commercial properties. Attached is a zip of the files.
For Business Card
Name: Morgan Tillsey
Position: Operations Manager
Number: 1 (506) 384-2971
Email: Morgan@harbrook.ca
Website: Harbrook.ca
Industry/Entity Type
Property Management

```html
<!DOCTYPE html>
<html lang="en">
<head>
<meta charset="UTF-8">
<title>Harbrook Property Management – Letterhead</title>
<link rel="stylesheet" href="https://fonts.googleapis.com/css2?family=Montserrat:wght@400;600;700&display=swap">
<style>
  :root {
    --backdrop: #e9e9e9;
    --paper: #ffffff;
    --brand-green: #84ab3a;
    --brand-green-soft: #9cbf58;
    --ink: #151515;
    --muted: #2a2a2a;
  }
  * { margin: 0; padding: 0; box-sizing: border-box; }
  html, body {
    width: 1200px;
    height: 874px;
    overflow: hidden;
    background: var(--backdrop);
    font-family: "Montserrat", Arial, sans-serif;
  }
  .letterhead {
    position: absolute;
    left: 310px;
    top: 27px;
    width: 580px;
    height: 820px;
    background: var(--paper);
    box-shadow: 0 6px 24px rgba(0,0,0,0.12);
    overflow: hidden;
  }
  .brand {
    position: absolute;
    left: 44px;
    top: 62px;
    display: flex;
    align-items: center;
    gap: 10px;
  }
  .brand-dot {
    width: 12px;
    height: 12px;
    border-radius: 50%;
    background: var(--brand-green);
  }
  .brand-name {
    font-weight: 700;
    font-size: 30px;
    letter-spacing: 2px;
    color: var(--ink);
    text-transform: uppercase;
    line-height: 1;
  }
  .contact {
    position: absolute;
    right: 44px;
    top: 52px;
    padding-left: 12px;
    border-left: 1px solid var(--brand-green);
    font-style: normal;
    font-size: 9.5px;
    line-height: 1.55;
    color: var(--muted);
  }
  .contact-name {
    color: var(--brand-green);
    font-weight: 700;
    text-transform: uppercase;
    font-size: 10px;
  }
  .contact-role { margin-bottom: 2px; }
  .contact-line { display: flex; align-items: center; gap: 6px; }
  .contact-icon { width: 9px; height: 9px; flex: none; }
  .footer-band {
    position: absolute;
    left: 0;
    bottom: 0;
    width: 100%;
    height: 150px;
    background: linear-gradient(90deg, var(--brand-green-soft), var(--brand-green));
  }
</style>
</head>
<body>
  <main class="letterhead">
    <header class="brand">
      <span class="brand-dot"></span>
      <span class="brand-name">Harbrook</span>
    </header>

    <address class="contact">
      <div class="contact-name">Morgan Tillsey</div>
      <div class="contact-role">Operations Manager</div>
      <div class="contact-line">
        <svg class="contact-icon" viewBox="0 0 10 10"><path d="M2 1 L4 1 L4.6 3 L3.5 4 Q4.5 6 6 6.5 L7 5.4 L9 6 L9 8 Q8.5 9 7.5 9 Q1 8 1 2.5 Q1 1 2 1Z" fill="var(--brand-green)"/></svg>
        <span>1 (506) 384-2971</span>
      </div>
      <div class="contact-line">
        <svg class="contact-icon" viewBox="0 0 10 10"><rect x="0.5" y="2" width="9" height="6.5" rx="1" fill="var(--brand-green)"/><path d="M0.8 2.5 L5 5.8 L9.2 2.5" stroke="#fff" stroke-width="0.9" fill="none"/></svg>
        <span>Morgan@harbrook.ca</span>
      </div>
      <div class="contact-line">
        <svg class="contact-icon" viewBox="0 0 10 10"><circle cx="5" cy="5" r="4.3" fill="var(--brand-green)"/><path d="M0.8 5 H9.2 M5 0.8 Q2.5 5 5 9.2 M5 0.8 Q7.5 5 5 9.2" stroke="#fff" stroke-width="0.7" fill="none"/></svg>
        <span>Harbrook.ca</span>
      </div>
    </address>

    <div class="footer-band" role="img" aria-label="Decorative green wave footer in brand colours"></div>
  </main>
</body>
</html>
```